Exciting product design for natural pet treats

We need a design for our stand up doy style pouch that blends well with our current logo and also bold enough to stand out from the crowd.

We have a range of natural, Australian made pet treats and need a generic bag that allows for a sticker to be placed on the bag to idenfity the name, while also allowing a space for another sticker on the back for ingredients.
___
Information for the front is: logo, Australian made and owned, Pet Food Only (this is a small font and should not be hero text), 100% Natural, Visit our web site for more amazing products for your pets, Space for sticker 100 - 150mm x 30mm.
___
Information for the back is: Kibblo Nest is proudly Australian owned and operated. We source all our Kibblo Nest treats from reputable suppliers around Australia.

Our Kibblo Nest treats can be purchased through our online store, where you will find a growing range of other brands and products for your dogs, cats, birds, fish, rabbits, guinea pigs, horses, cows, sheep, chickens and more.

For further information, please visit our web site www.kibblonest.com.au or email us directly info@kibblonest.com.au.
____
The design will be used on three different bag sizes, so our printer can reduce the design from the largest size, but please keep in mind the sizes are 280mm x 380mm, 190mm x 275mm & 160mm x 230mm.

Target Market(s)

Mostly female, 25 to 65 years of age. Pet Lovers, particuarly focussing on dogs.

Industry/Entity Type

pet industry

Requirements
Must have
• Space for sticker on front for the product name 100mm x 30mm. Also a
Nice to have
• Space for a window.
Should not have
• comical pet images. Does not need an image of a pet. Does not need an image of the food.

```html
<!DOCTYPE html>
<html lang="en">
<head>
<meta charset="utf-8">
<title>Kibblo Nest – Treat Pouch</title>
<link href="https://fonts.googleapis.com/css2?family=Poppins:wght@400;500;600&family=Oswald:wght@400&display=swap" rel="stylesheet">
<style>
  :root{
    --teal:#4ea6ad;
    --teal-dark:#3f9299;
    --purple:#4b2069;
    --purple-text:#4a2570;
    --white:#ececec;
    --stage:#8f8f8f;
    --ink:#1e1e1e;
  }
  *{margin:0;padding:0;box-sizing:border-box}
  html,body{width:1200px;height:800px;overflow:hidden}
  body{background:var(--stage);position:relative;font-family:"Poppins",sans-serif}
  .pouch{position:absolute;top:80px;width:412px;height:650px}
  .pouch--front{left:140px}
  .pouch--back{left:640px}
  .pouch__shape{position:absolute;inset:0}
  .brand{position:absolute;top:150px;left:0;width:100%;display:flex;justify-content:center;align-items:center;gap:10px}
  .brand__mark{width:56px;height:56px;border:4px solid var(--teal);border-radius:50%}
  .brand__name{font-weight:600;font-size:36px;color:var(--purple-text);letter-spacing:-0.5px}
  .sticker{position:absolute;background:#efefef;border:1px solid #b9b9b9;border-radius:8px;
    box-shadow:0 1px 3px rgba(0,0,0,.2);display:flex;justify-content:center;
    font-family:"Oswald",sans-serif;font-size:13px;color:var(--ink)}
  .sticker--name{left:96px;top:253px;width:214px;height:68px;align-items:center}
  .sticker--ingredients{left:99px;top:497px;width:204px;height:99px;padding-top:24px;border-radius:10px}
  .food-window{position:absolute;left:19px;top:336px;width:372px;height:116px;
    background:linear-gradient(100deg,#b77445,#d8a06c 30%,#a85f35 55%,#cf9060 80%,#b06a3c);
    clip-path:polygon(0 4%,100% 0,100% 86%,0 100%)}
  .pet-food{position:absolute;left:270px;top:458px;font-size:11px;color:var(--purple-text);transform:rotate(-5deg)}
  .natural-badge{position:absolute;left:66px;top:434px;width:86px;height:86px}
  .made-badge{position:absolute;left:0;width:100%;top:520px;text-align:center;color:#fff}
  .made-badge__shape{width:40px;height:26px;margin:0 auto 4px;background:#fff;border-radius:40% 55% 45% 50%}
  .made-badge__title{font-weight:600;font-size:8.5px;letter-spacing:.3px;line-height:1}
  .made-badge__sub{font-size:5.5px;letter-spacing:.3px}
  .visit-pill{position:absolute;left:91px;top:573px;width:222px;height:32px;background:var(--teal);
    border-radius:16px;transform:rotate(-2deg);color:#fff;font-size:9px;line-height:11px;
    text-align:center;padding-top:5px;letter-spacing:.2px}
  .about{position:absolute;top:270px;left:50px;width:312px;text-align:center;color:var(--purple-text);
    font-size:9px;line-height:13.5px}
  .about p{margin-bottom:11px}
  .about strong{font-weight:600}
  .about .link{color:var(--teal-dark);font-weight:600;display:block}
</style>
</head>
<body>

<section class="pouch pouch--front">
  <svg class="pouch__shape" viewBox="0 0 412 650" aria-hidden="true">
    <defs><clipPath id="front-clip"><path d="M14 0H398Q412 0 412 14L412 70L384 612Q383 632 363 632L49 632Q29 632 28 612L0 70L0 14Q0 0 14 0Z"/></clipPath></defs>
    <g clip-path="url(#front-clip)">
      <rect width="412" height="650" fill="var(--white)"/>
      <rect width="412" height="66" fill="var(--teal)"/>
      <line x1="18" y1="84" x2="394" y2="84" stroke="#d2d2d2" stroke-width="2"/>
      <line x1="18" y1="90" x2="394" y2="90" stroke="#d8d8d8" stroke-width="1.5"/>
      <path d="M0 470C80 460 160 462 230 482S360 517 412 497L412 650L0 650Z" fill="var(--teal)"/>
      <path d="M0 478C80 470 160 474 230 494S360 527 412 508L412 650L0 650Z" fill="var(--purple)"/>
    </g>
  </svg>

  <div class="brand"><span class="brand__mark"></span><span class="brand__name">Kibblo Nest</span></div>
  <div class="sticker sticker--name">Space for sticker</div>
  <div class="food-window" role="img" aria-label="Product window showing the dried natural treats inside"></div>
  <div class="pet-food">Pet Food Only</div>

  <svg class="natural-badge" viewBox="0 0 86 86" aria-label="100% Natural">
    <defs><path id="badge-arc" d="M12 43A31 31 0 0 0 74 43"/></defs>
    <circle cx="43" cy="43" r="42" fill="var(--teal)"/>
    <circle cx="43" cy="43" r="37" fill="none" stroke="#fff" stroke-width="1.5"/>
    <path d="M43 56C33 52 28 44 30 34C38 36 43 44 43 56Z" fill="#fff"/>
    <path d="M43 56C45 42 52 34 62 32C62 44 55 53 43 56Z" fill="#fff"/>
    <text font-family="Poppins,sans-serif" font-size="7.5" fill="#fff" letter-spacing="1"><textPath href="#badge-arc" startOffset="50%" text-anchor="middle">100 % NATURAL</textPath></text>
  </svg>

  <div class="made-badge">
    <div class="made-badge__shape"></div>
    <div class="made-badge__title">AUSTRALIAN</div>
    <div class="made-badge__sub">MADE AND OWNED</div>
  </div>
  <div class="visit-pill">VISIT OUR WEB SITE FOR MORE AMAZING<br>PRODUCTS FOR YOUR PETS</div>
</section>

<section class="pouch pouch--back">
  <svg class="pouch__shape" viewBox="0 0 412 650" aria-hidden="true">
    <defs><clipPath id="back-clip"><path d="M14 0H398Q412 0 412 14L412 70L384 612Q383 632 363 632L49 632Q29 632 28 612L0 70L0 14Q0 0 14 0Z"/></clipPath></defs>
    <g clip-path="url(#back-clip)">
      <rect width="412" height="650" fill="var(--white)"/>
      <rect width="412" height="66" fill="var(--teal)"/>
      <line x1="18" y1="84" x2="394" y2="84" stroke="#d2d2d2" stroke-width="2"/>
      <line x1="18" y1="90" x2="394" y2="90" stroke="#d8d8d8" stroke-width="1.5"/>
      <path d="M0 477C90 466 170 472 240 490S360 520 412 500L412 650L0 650Z" fill="var(--teal)"/>
      <path d="M0 485C90 476 170 483 240 500S360 530 412 511L412 650L0 650Z" fill="var(--purple)"/>
    </g>
  </svg>

  <div class="brand"><span class="brand__mark"></span><span class="brand__name">Kibblo Nest</span></div>
  <div class="about">
    <p><strong>Kibblo Nest</strong> is proudly Australian owned and operated. We source all our Kibblo Nest treats from reputable suppliers around Australia.</p>
    <p>Our <strong>Kibblo Nest</strong> treats can be purchased through our online store, where you will find a growing range of other brands and products for your dogs, cats, birds, fish, rabbits, guinea pigs, horses, cows, sheep, chickens and more.</p>
    <p>For further information, please visit our web site<span class="link">www.kibblonest.com.au</span></p>
    <p>or email us directly<span class="link">info@kibblonest.com.au.</span></p>
  </div>
  <div class="sticker sticker--ingredients">Space for ingredients sticker</div>
</section>

</body>
</html>
```